Restaurant needs a vertical banner for fried catfish

Our restaurant is looking for an eye-catching 78.75in. x 36in. vertical physical banner ad for our fried catfish. Photos for the fried catfish will be provided as a reference but we will also accept anything similar to the photo. We will be using the following as our receptacle: https://www.plankoria.example/banner-stand/retractable-banner-stands/
The design must incorporate the following flavor texts:
Fried Catfish
Always Fresh!
Made from Scratch
Hand-cut Fillets
The Best Catfish in Texas
Served with fries, hush puppies, and a 32oz fountain drink
Also available by the pound!
The final design should be creative, professional, and eye-catching for customers.
Updates
Colors
Designer to choose colors to be used in the design.
Requirements
Must have
- We are open to any and all design elements, albeit the 'flavor texts' should not overpower, but complement the fried catfish photo. 'Fried Catfish' can be used in lieu of a main title/logo.
Nice to have
- Transparent or textured backgrounds that can encompass any or all part of the banner such as a cutting board, shadows, abstract, etc to show depth are a plus.
- Use of vectors or objects such as ribbons or shapes to encapsulate the 'flavor texts' are also encouraged.

```html
<!DOCTYPE html>
<html lang="en">
<head>
<meta charset="utf-8">
<title>Fried Catfish Vertical Banner</title>
<link rel="stylesheet" href="https://fonts.googleapis.com/css2?family=Kaushan+Script&family=Alfa+Slab+One&family=Amatic+SC:wght@700&family=Oswald:wght@500&display=swap">
<style>
  :root {
    --page-bg: #e4e4e4;
    --wood-dark: #2e1b12;
    --wood-mid: #4a2e20;
    --brand-red: #ec1c2e;
    --brand-orange: #f47b20;
    --brand-yellow: #e6e621;
    --ink-brown: #3a2219;
    --white: #ffffff;
    --fish-gold: #b0702a;
    --fish-deep: #7a4418;
  }
  html, body {
    margin: 0;
    width: 1200px;
    height: 857px;
    overflow: hidden;
    background: var(--page-bg);
  }
  .canvas {
    position: relative;
    width: 1200px;
    height: 857px;
  }
  .banner {
    position: absolute;
    left: 478px;
    top: 28px;
    width: 244px;
    height: 800px;
    display: block;
  }
  .script { font-family: "Kaushan Script", cursive; }
  .slab { font-family: "Alfa Slab One", serif; }
  .hand { font-family: "Amatic SC", sans-serif; font-weight: 700; }
  .condensed { font-family: "Oswald", sans-serif; font-weight: 500; }
</style>
</head>
<body>
<div class="canvas">
  <svg class="banner" viewBox="0 0 244 800" xmlns="http://www.w3.org/2000/svg">
    <defs>
      <linearGradient id="wood" x1="0" y1="0" x2="1" y2="0">
        <stop offset="0" stop-color="var(--wood-dark)"/>
        <stop offset="0.3" stop-color="var(--wood-mid)"/>
        <stop offset="0.55" stop-color="var(--wood-dark)"/>
        <stop offset="0.8" stop-color="var(--wood-mid)"/>
        <stop offset="1" stop-color="var(--wood-dark)"/>
      </linearGradient>
      <radialGradient id="fishTone" cx="0.6" cy="0.45" r="0.7">
        <stop offset="0" stop-color="var(--fish-gold)"/>
        <stop offset="1" stop-color="var(--fish-deep)"/>
      </radialGradient>
      <clipPath id="bannerClip"><rect width="244" height="800"/></clipPath>
    </defs>

    <g clip-path="url(#bannerClip)">
      <rect class="wood-backdrop" width="244" height="800" fill="url(#wood)" role="img" aria-label="Dark wooden plank texture"/>

      <g class="hero-photo">
        <circle cx="150" cy="150" r="174" fill="var(--brand-orange)"/>
        <circle cx="153" cy="150" r="165" fill="var(--brand-red)"/>
        <circle cx="160" cy="148" r="152" fill="url(#fishTone)" role="img" aria-label="Close-up photo of cornmeal-fried catfish fillets over fries"/>
      </g>

      <g class="title-badge">
        <circle cx="79" cy="77" r="60" fill="none" stroke="var(--brand-red)" stroke-width="1.2"/>
        <circle cx="79" cy="77" r="56" fill="var(--brand-yellow)"/>
        <text class="script" x="80" y="78" font-size="42" fill="var(--ink-brown)" text-anchor="middle" textLength="86" lengthAdjust="spacingAndGlyphs" transform="rotate(-8 80 78)">Fried</text>
        <text class="slab" x="81" y="104" font-size="18" fill="var(--ink-brown)" text-anchor="middle" textLength="90" lengthAdjust="spacingAndGlyphs" transform="rotate(-6 81 104)">CATFISH</text>
      </g>

      <g class="headline">
        <text class="script" x="57" y="290" font-size="25" fill="var(--white)">The</text>
        <text class="script" x="32" y="342" font-size="56" fill="var(--brand-yellow)" textLength="92" lengthAdjust="spacingAndGlyphs">BEST</text>
        <text class="script" x="133" y="336" font-size="32" fill="var(--white)" textLength="95" lengthAdjust="spacingAndGlyphs">Catfish</text>
        <polygon points="40,349 235,349 225,373 235,398 32,398 42,373" fill="var(--brand-red)"/>
        <text class="slab" x="34" y="372" font-size="13" fill="var(--white)" text-anchor="middle" transform="rotate(-90 34 372)" dy="4">in</text>
        <text class="slab" x="133" y="392" font-size="44" fill="var(--ink-brown)" text-anchor="middle" textLength="165" lengthAdjust="spacingAndGlyphs">TEXAS</text>
      </g>

      <g class="claims">
        <text class="hand" x="121" y="447" font-size="32" fill="var(--white)" text-anchor="middle" textLength="125" lengthAdjust="spacingAndGlyphs">ALWAYS FRESH!</text>
        <text class="hand" x="121" y="482" font-size="32" fill="var(--white)" text-anchor="middle" textLength="182" lengthAdjust="spacingAndGlyphs">MADE FROM SCRATCH!</text>
      </g>

      <g class="plate-photo">
        <ellipse cx="118" cy="586" rx="119" ry="88" fill="var(--brand-orange)"/>
        <ellipse cx="116" cy="588" rx="112" ry="78" fill="url(#fishTone)" role="img" aria-label="Photo of a plate of fried catfish fillets with fries, hush puppies and tartar sauce"/>
        <polygon points="148,629 244,629 244,646 148,646 156,637.5" fill="var(--brand-red)"/>
        <text class="condensed" x="198" y="642" font-size="11" fill="var(--white)" text-anchor="middle">Hand-Cut Fillets</text>
      </g>

      <g class="serving">
        <text class="hand" x="233" y="701" font-size="21" fill="var(--brand-yellow)" text-anchor="end" textLength="169" lengthAdjust="spacingAndGlyphs">SERVED WITH FRIES, HUSH PUPPIES,</text>
        <text class="hand" x="236" y="725" font-size="21" fill="var(--brand-yellow)" text-anchor="end" textLength="144" lengthAdjust="spacingAndGlyphs">AND A 32OZ FOUNTAIN DRINK</text>
      </g>

      <g class="footer-band">
        <rect x="0" y="750" width="244" height="50" fill="var(--brand-red)"/>
        <rect x="0" y="746" width="244" height="4" fill="var(--brand-orange)"/>
        <text class="condensed" x="122" y="783" font-size="20" fill="var(--white)" text-anchor="middle" textLength="206" lengthAdjust="spacingAndGlyphs">Also available by the pound!</text>
      </g>
    </g>
  </svg>
</div>
</body>
</html>
```